Extend Medium Rectangle into Halfpage and Billboard Ad Format

We have a few variations of our Medium Rectangle (300x250) that we use to build scalable online ads for local advertisers based on their images and logos which in most of the cases are very basic but still should deliver decent results in terms of overall banner look.

Based on those variations we would like to have each a Halfpage and Billboard variation to it that resembles the "look & feel" to feel like "out of one hand" and allows the local advertiser to recognize his ad across all formats.

Core of the Medium Rectangle is a carousel ad to swipe through the images and "more information" for the click-out to the landingpage. That might be great to replicate on the other banner formats but also could be done differently.

Attached the examples we have for one local customer to build ads from. Very limited but realistic.

```html
<!DOCTYPE html>
<html lang="de">
<head>
<meta charset="utf-8">
<title>Gasthof Linde – Banner</title>
<link href="https://fonts.googleapis.com/css2?family=Rubik:wght@500;700&display=swap" rel="stylesheet">
<style>
  :root {
    --brand-red: #d0062f;
    --ink: #111111;
    --paper: #ffffff;
    --dash-idle: #e4e4e4;
    --shadow: rgba(0,0,0,0.45);
  }
  * { margin: 0; padding: 0; box-sizing: border-box; }
  html, body { width: 1200px; height: 1000px; overflow: hidden; background: var(--paper); }
  body { position: relative; font-family: "Rubik", sans-serif; }

  .banner {
    position: absolute;
    left: 254px;
    width: 693px;
    height: 217px;
    background: var(--paper);
    box-shadow: 2px 2px 2px var(--shadow);
    overflow: hidden;
  }
  .banner--house { top: 133px; }
  .banner--interior { top: 391px; }
  .banner--dish { top: 649px; }

  .banner__photo {
    position: absolute;
    inset: 0 auto 0 0;
    width: 491px;
    height: 217px;
    clip-path: polygon(0 0, 491px 0, 430px 217px, 0 217px);
  }
  .banner--house .banner__photo {
    background: linear-gradient(180deg, #eef0f2 0%, #e6e3dc 35%, #d9cf94 55%, #8b6b4e 80%, #5c5a4c 100%);
  }
  .banner--interior .banner__photo {
    background: linear-gradient(180deg, #c9a878 0%, #8e5a2e 35%, #6b1a1c 60%, #2a1b16 80%, #b8a48c 100%);
  }
  .banner--dish .banner__photo {
    background: radial-gradient(ellipse at 55% 60%, #c98a3e 0%, #9a5a2c 40%, #e8dccb 75%, #f3ede6 100%);
  }

  .banner__brand {
    position: absolute;
    left: 577px;
    top: 36px;
    font-weight: 500;
    font-size: 28px;
    letter-spacing: 0.5px;
    color: var(--brand-red);
  }

  .banner__cta {
    position: absolute;
    left: 390px;
    top: 83px;
    width: 136px;
    height: 29px;
    background: var(--brand-red);
    clip-path: polygon(0 0, 136px 0, 128px 29px, 0 29px);
    color: var(--paper);
    font-weight: 700;
    font-size: 16px;
    line-height: 29px;
    padding-left: 9px;
    text-decoration: none;
  }

  .banner__dots {
    position: absolute;
    top: 129px;
    left: 423px;
    display: flex;
    gap: 6px;
  }
  .banner__dot { width: 20px; height: 4px; background: var(--dash-idle); }
  .banner__dot--active { background: var(--brand-red); }
  .banner--interior .banner__dots { left: 449px; }

  .banner__headline {
    position: absolute;
    left: 526px;
    top: 121px;
    font-weight: 700;
    font-size: 21px;
    line-height: 28px;
    color: var(--ink);
  }
  .banner__headline-accent { color: var(--brand-red); display: block; }
</style>
</head>
<body>

  <section class="banner banner--house">
    <div class="banner__photo" role="img" aria-label="Außenansicht des Gasthofs mit gelber Fassade und rotem Dach"></div>
    <div class="banner__brand">LINDE</div>
    <a class="banner__cta" href="#">Mehr erfahren</a>
    <div class="banner__dots">
      <span class="banner__dot banner__dot--active"></span>
      <span class="banner__dot"></span>
      <span class="banner__dot"></span>
    </div>
    <h2 class="banner__headline">
      Neueröffnung
      <span class="banner__headline-accent">Gasthof Linde</span>
      in Lindenau!
    </h2>
  </section>

  <section class="banner banner--interior">
    <div class="banner__photo" role="img" aria-label="Gastraum mit gedeckten Tischen, roten Stühlen und Vorhängen"></div>
    <div class="banner__brand">LINDE</div>
    <a class="banner__cta" href="#">Mehr erfahren</a>
    <div class="banner__dots">
      <span class="banner__dot banner__dot--active"></span>
      <span class="banner__dot"></span>
    </div>
  </section>

  <section class="banner banner--dish">
    <div class="banner__photo" role="img" aria-label="Nahaufnahme eines angerichteten Gerichts mit Kräutergarnitur"></div>
    <div class="banner__brand">LINDE</div>
    <a class="banner__cta" href="#">Mehr erfahren</a>
    <div class="banner__dots">
      <span class="banner__dot"></span>
      <span class="banner__dot"></span>
      <span class="banner__dot banner__dot--active"></span>
    </div>
  </section>

</body>
</html>
```